I need to add on from our previous project a couple extra signs

We need to create two signs from your original desgin with a arrow saying 600M on the left.
also another sign drawn up similar to the one attached but also adding in there that the containers are 20ft/40ft and we have caravan, car and boat storage.
also add on the sign something for " sign online or call the number to rent space"

```html
<!DOCTYPE html>
<html lang="en">
<head>
<meta charset="utf-8">
<title>Keystone Storage – Shipping Container Storage Sign</title>
<link rel="stylesheet" href="https://fonts.googleapis.com/css2?family=Barlow+Condensed:ital,wght@0,800;1,300;1,800&family=Montserrat:wght@600&display=swap">
<style>
  :root {
    --brand-red: #c8202a;
    --deep-red: #8a0b12;
    --ink: #231f20;
    --paper: #ffffff;
    --backdrop: #e4e4e4;
  }
  html, body {
    margin: 0;
    padding: 0;
    width: 1200px;
    height: 1200px;
    overflow: hidden;
    background: var(--backdrop);
  }
  .canvas {
    position: relative;
    width: 1200px;
    height: 1200px;
  }
  .sign {
    position: absolute;
    left: 37px;
    top: 289px;
    width: 1126px;
    height: 623px;
    overflow: hidden;
    background: var(--paper);
  }
  .sign-art {
    position: absolute;
    inset: 0;
    width: 100%;
    height: 100%;
  }
  .txt {
    position: absolute;
    margin: 0;
    line-height: 1;
    white-space: nowrap;
    font-family: "Barlow Condensed", "Arial Narrow", sans-serif;
    color: var(--paper);
  }
  .heading {
    font-weight: 800;
    font-style: italic;
    font-size: 57px;
    right: 706px;
    top: 313px;
    letter-spacing: -1px;
  }
  .intro {
    font-weight: 300;
    font-style: italic;
    font-size: 54px;
    right: 713px;
    text-align: right;
    top: 364px;
    line-height: 49px;
  }
  .threat-label {
    font-weight: 800;
    font-style: italic;
    font-size: 37px;
    top: 429px;
    width: 140px;
    text-align: center;
    letter-spacing: -0.5px;
  }
  .divider {
    position: absolute;
    left: 91px;
    top: 472px;
    width: 969px;
    height: 2px;
    background: var(--paper);
  }
  .spec-title {
    font-weight: 300;
    font-style: italic;
    font-size: 54px;
    top: 490px;
  }
  .spec-title--size { right: 723px; }
  .spec-title--type { left: 541px; }
  .spec-value {
    font-weight: 800;
    font-style: italic;
    font-size: 63px;
    top: 544px;
    letter-spacing: -1.5px;
  }
  .spec-value--size { right: 731px; }
  .spec-value--type { left: 538px; }
  .call-to-action {
    font-weight: 800;
    font-style: italic;
    font-size: 44px;
    color: var(--ink);
    right: 686px;
    top: 788px;
    text-align: right;
    line-height: 43px;
    letter-spacing: -0.5px;
  }
  .brand-mark {
    position: absolute;
    left: 563px;
    top: 719px;
    width: 160px;
    height: 160px;
    border-radius: 50%;
    background: var(--brand-red);
  }
  .brand-name {
    font-weight: 800;
    font-size: 62px;
    color: var(--ink);
    left: 741px;
    top: 713px;
    line-height: 54px;
    letter-spacing: 1px;
  }
  .brand-web {
    font-family: "Montserrat", Arial, sans-serif;
    font-weight: 600;
    font-size: 19px;
    color: var(--ink);
    left: 743px;
    top: 827px;
    letter-spacing: 0.6px;
  }
  .brand-phone {
    font-family: "Montserrat", Arial, sans-serif;
    font-weight: 600;
    font-size: 26px;
    color: var(--brand-red);
    left: 743px;
    top: 852px;
    letter-spacing: 4px;
  }
</style>
</head>
<body>
<main class="canvas">
  <section class="sign" aria-label="Shipping container storage sign">
    <svg class="sign-art" viewBox="0 0 1812 1003" preserveAspectRatio="none" xmlns="http://www.w3.org/2000/svg">
      <defs>
        <linearGradient id="warehouseTone" x1="0" y1="0" x2="1" y2="0.3">
          <stop offset="0" stop-color="#8c0f14"/>
          <stop offset="0.45" stop-color="#6a070b"/>
          <stop offset="0.75" stop-color="#3a0305"/>
          <stop offset="1" stop-color="#120102"/>
        </linearGradient>
        <linearGradient id="bandTone" x1="0" y1="0" x2="0" y2="1">
          <stop offset="0" stop-color="#9a1219"/>
          <stop offset="1" stop-color="#d0222c"/>
        </linearGradient>
        <linearGradient id="paperTone" x1="0" y1="0" x2="0" y2="1">
          <stop offset="0" stop-color="#dedede"/>
          <stop offset="1" stop-color="#ffffff"/>
        </linearGradient>
      </defs>
      <rect class="paper" x="0" y="0" width="1812" height="1003" fill="url(#paperTone)"/>
      <polygon class="warehouse-photo" role="img" aria-label="Photo of a storage warehouse with rows of wooden storage crates, tinted red"
               points="0,0 1812,0 1812,440 520,700 0,495" fill="url(#warehouseTone)"/>
      <polygon class="red-swoosh" points="0,495 520,700 1812,440 1812,542 520,712 0,605" fill="url(#bandTone)"/>
      <rect class="footer-band" x="0" y="980" width="1812" height="23" fill="#c8202a"/>
    </svg>

    <!-- benefit icons: ring frames with artwork areas -->
    <svg class="sign-art" viewBox="0 0 1126 623" xmlns="http://www.w3.org/2000/svg">
      <g fill="none" stroke="#ffffff" stroke-width="3.5">
        <circle cx="557" cy="79" r="54"/>
        <circle cx="693" cy="79" r="54"/>
        <circle cx="831" cy="79" r="54"/>
        <circle cx="967" cy="79" r="54"/>
      </g>
      <g fill="#ffffff" fill-opacity="0.1">
        <circle cx="557" cy="79" r="40" role="img" aria-label="Icon of a rat"/>
        <circle cx="693" cy="79" r="40" role="img" aria-label="Icon of a cockroach"/>
        <circle cx="831" cy="79" r="40" role="img" aria-label="Icon of an umbrella"/>
        <circle cx="967" cy="79" r="40" role="img" aria-label="Icon of a dust cloud"/>
      </g>
    </svg>
  </section>

  <h1 class="txt heading">WHY CHOOSE US ?</h1>
  <p class="txt intro">SHIPPING CONTAINERS<br>ARE FREE FROM</p>

  <span class="txt threat-label" style="left:524px">VERMIN</span>
  <span class="txt threat-label" style="left:660px">INSECTS</span>
  <span class="txt threat-label" style="left:798px">WATER</span>
  <span class="txt threat-label" style="left:934px">DUST</span>

  <div class="divider"></div>

  <p class="txt spec-title spec-title--size">CONTAINER SIZE</p>
  <p class="txt spec-title spec-title--type">STORAGE TYPE</p>
  <p class="txt spec-value spec-value--size">20ft x 40ft</p>
  <p class="txt spec-value spec-value--type">CARAVAN • CAR • BOAT</p>

  <p class="txt call-to-action">SIGN ONLINE OR CALL THE<br>NUMBER TO RENT SPACE</p>

  <div class="brand-mark" aria-hidden="true"></div>
  <p class="txt brand-name">KEYSTONE<br>STORAGE</p>
  <p class="txt brand-web">www.keystonestorage.com.au</p>
  <p class="txt brand-phone">(03) 5550 0147</p>
</main>
</body>
</html>
```